Flyer Design Dental Office Grand Opening offer

Dental office.

Grand opening flyer. Offer Exam + cleaning + xrays.
special: free teeth whitening ($200 value)

Target Market(s)

Middle class people around Huntington Beach.

Industry/Entity Type

Dental Clinic

Colors
cfeae6
86cfc6
fac994
fee18a
e667a6

Requirements
Must have
• Do not change my existing logo
Nice to have
• Have some appealing picture/design to catch the eye, but not too flashy
Should not have
• No cartoon kind of design

```html
<!DOCTYPE html>
<html lang="en">
<head>
<meta charset="utf-8">
<title>Harbor Dental – Grand Opening Flyer</title>
<link rel="stylesheet" href="https://fonts.googleapis.com/css2?family=Lato:wght@400;700&family=Oswald:wght@500;600;700&family=Roboto+Slab:wght@900&display=swap">
<style>
  :root {
    --page-bg: #9a9a9a;
    --paper: #ffffff;
    --ink: #2f2f2f;
    --teal: #1ea6b8;
    --teal-light: #4cc0cf;
    --orange: #f26a2c;
    --orange-dark: #d9521b;
    --orange-light: #f98a4d;
    --peach: #f9c891;
    --photo-a: #e8ecef;
    --photo-b: #cfd8dc;
    --floor: #efefef;
  }
  * { box-sizing: border-box; margin: 0; padding: 0; }
  html, body { width: 1200px; height: 1200px; overflow: hidden; }
  body { background: var(--page-bg); position: relative; font-family: "Lato", sans-serif; color: var(--ink); }

  .flyer {
    position: absolute; left: 201px; top: 40px;
    width: 920px; height: 1290px;
    background: var(--paper);
    transform: scale(0.868); transform-origin: top left;
    overflow: hidden;
  }

  /* header */
  .brand { position: absolute; left: 28px; top: 50px; display: flex; align-items: center; gap: 14px; }
  .brand-mark { width: 54px; height: 54px; background: var(--teal); }
  .brand-name { font-family: "Lato", sans-serif; font-weight: 700; font-size: 46px; line-height: 1; color: var(--teal); letter-spacing: 1px; }
  .brand-doctor { position: absolute; left: 241px; top: 133px; width: 126px; text-align: right; font-size: 15px; line-height: 18px; color: #222; }

  .contact { position: absolute; left: 540px; top: 40px; }
  .contact-row { display: flex; align-items: flex-start; gap: 14px; color: var(--ink); }
  .contact-phone { font-size: 26px; font-weight: 700; line-height: 34px; }
  .contact-address { margin-top: 14px; font-size: 20px; font-weight: 700; line-height: 25px; }
  .contact-row svg { flex: none; margin-top: 6px; }

  /* hero */
  .hero-photo {
    position: absolute; left: 0; top: 185px; width: 920px; height: 483px;
    background: linear-gradient(100deg, var(--photo-b) 0%, var(--photo-a) 45%, #dfe5e8 100%);
  }
  .stage {
    position: absolute; left: 0; top: 668px; width: 920px; height: 340px;
    background: linear-gradient(180deg, var(--floor) 0%, #ffffff 70%);
  }
  .rule { position: absolute; left: 55px; top: 684px; width: 790px; height: 8px; background: var(--teal); }

  .banner { position: absolute; left: 0; top: 0; width: 920px; height: 1000px; }
  .headline { position: absolute; left: 160px; width: 610px; text-align: center; color: #fff; line-height: 1; text-shadow: 2px 3px 0 rgba(150,50,10,.35); }
  .headline-grand { top: 594px; font-family: "Roboto Slab", serif; font-weight: 900; font-size: 96px; letter-spacing: 8px; }
  .headline-opening { top: 698px; font-family: "Oswald", sans-serif; font-weight: 700; font-size: 134px; letter-spacing: 1px; transform: rotate(1deg); }

  /* offer */
  .price-badge { position: absolute; left: 28px; top: 993px; width: 284px; height: 260px; }
  .price-amount { position: absolute; left: 0; width: 336px; top: 1030px; text-align: center; font-family: "Oswald", sans-serif; font-weight: 700; font-size: 80px; line-height: 80px; color: #fff; }
  .price-free { position: absolute; left: 0; width: 336px; top: 1138px; text-align: center; font-family: "Lato", sans-serif; font-weight: 700; font-size: 48px; line-height: 48px; color: #fff; }

  .offer-item { position: absolute; display: flex; align-items: flex-start; gap: 14px; }
  .offer-text {
    font-size: 32px; font-weight: 700; color: var(--ink); line-height: 40px;
    padding: 8px 6px 8px 8px; white-space: nowrap;
    background: linear-gradient(90deg, rgba(249,200,145,0) 0%, rgba(249,200,145,.55) 50%, var(--peach) 100%);
  }
  .offer-exam { left: 350px; top: 998px; }
  .offer-exam .offer-text { width: 453px; }
  .offer-bleach { left: 334px; top: 1075px; }
  .offer-bleach .offer-text { width: 485px; }

  .special {
    position: absolute; left: 367px; top: 1176px; width: 519px; height: 67px;
    background: var(--teal); padding: 6px;
  }
  .special-inner {
    height: 100%; border: 2px dashed #fff;
    display: flex; align-items: center; justify-content: center;
    font-family: "Oswald", sans-serif; font-weight: 600; font-size: 25px; color: #fff; letter-spacing: .2px;
  }
  .footer-band { position: absolute; left: 0; bottom: 0; width: 920px; height: 15px; background: var(--teal); }
</style>
</head>
<body>
<main class="flyer">
  <header>
    <div class="brand">
      <span class="brand-mark"></span>
      <span class="brand-name">Harbor Dental</span>
    </div>
    <p class="brand-doctor">Lena Tran, DDS</p>

    <div class="contact">
      <div class="contact-row contact-phone">
        <svg width="22" height="22" viewBox="0 0 24 24"><path fill="var(--teal)" d="M6.6 10.8a15 15 0 0 0 6.6 6.6l2.2-2.2c.3-.3.7-.4 1-.2 1.1.4 2.3.6 3.6.6.6 0 1 .4 1 1V20c0 .6-.4 1-1 1A17 17 0 0 1 3 4c0-.6.4-1 1-1h3.5c.6 0 1 .4 1 1 0 1.3.2 2.5.6 3.6.1.3 0 .7-.2 1z"/></svg>
        <span>(714) 555-0182</span>
      </div>
      <div class="contact-row contact-address">
        <svg width="18" height="24" viewBox="0 0 18 24"><path fill="var(--teal)" d="M9 0a8 8 0 0 0-8 8c0 6 8 16 8 16s8-10 8-16a8 8 0 0 0-8-8zm0 11a3 3 0 1 1 0-6 3 3 0 0 1 0 6z"/></svg>
        <span>1280 Seabreeze Ave., Huntington<br>Beach, CA 92648</span>
      </div>
    </div>
  </header>

  <div class="hero-photo" role="img" aria-label="Smiling patient in a dental chair giving a thumbs up in a bright clinic"></div>
  <div class="stage"></div>
  <div class="rule"></div>

  <svg class="banner" viewBox="0 0 920 1000" aria-hidden="true">
    <polygon points="475,460 650,455 755,550 460,540" fill="var(--orange-dark)"/>
    <polygon points="320,980 495,880 495,935" fill="var(--orange-dark)"/>
    <polygon points="320,980 495,935 300,920" fill="var(--orange)"/>
    <defs>
      <radialGradient id="bannerFill" cx="40%" cy="40%" r="70%">
        <stop offset="0" stop-color="var(--orange-light)"/>
        <stop offset="1" stop-color="var(--orange)"/>
      </radialGradient>
    </defs>
    <polygon points="160,517 755,550 765,865 210,890" fill="url(#bannerFill)"/>
  </svg>

  <h1>
    <span class="headline headline-grand">GRAND</span>
    <span class="headline headline-opening">OPENING</span>
  </h1>

  <section class="offer">
    <svg class="price-badge" viewBox="0 0 284 260" aria-hidden="true">
      <ellipse cx="142" cy="254" rx="90" ry="5" fill="rgba(0,0,0,.12)"/>
      <circle cx="140" cy="120" r="120" fill="var(--teal)"/>
      <circle cx="140" cy="120" r="110" fill="none" stroke="var(--teal-light)" stroke-width="3"/>
      <polygon points="0,145 20,115 264,115 284,145 264,200 20,200" fill="var(--orange)"/>
      <polygon points="20,115 264,115 258,125 26,125" fill="var(--orange-dark)"/>
    </svg>
    <p class="price-amount">$50</p>
    <p class="price-free">FREE</p>

    <div class="offer-item offer-exam">
      <svg width="36" height="40" viewBox="0 0 36 40"><rect x="3" y="3" width="22" height="28" rx="2" fill="none" stroke="var(--teal)" stroke-width="2"/><path d="M8 11h12M8 17h8" stroke="var(--teal)" stroke-width="2"/><path d="M18 22l6 6 9-4-2 10H20z" fill="none" stroke="var(--teal)" stroke-width="2"/></svg>
      <p class="offer-text">Exam&nbsp; with Xrays &amp; Cleaning</p>
    </div>
    <div class="offer-item offer-bleach">
      <svg width="52" height="46" viewBox="0 0 52 46"><path d="M2 30l16-18" stroke="var(--teal)" stroke-width="2"/><path d="M28 18c4-4 10-4 14 0 3 3 2 9 0 14l-2 10h-3l-2-8-2 8h-3l-2-10c-2-5-3-11 0-14z" fill="none" stroke="var(--teal)" stroke-width="2"/><path d="M36 6l2-4M42 9l4-2M30 8l-2-4" stroke="var(--teal)" stroke-width="2"/></svg>
      <p class="offer-text">Bleaching (after completion of<br>dental treatment</p>
    </div>

    <div class="special"><p class="special-inner">SPECIAL: FREE TEETH WHITENING ($200 VALUE)</p></div>
  </section>

  <div class="footer-band"></div>
</main>
</body>
</html>
```